Quillo App - Live Events Stream

Need mobile first appliation designs for a new location based events and offers application <br/><br/>Will require at least 5 screens creating, namely:<br/><br/>- Landing screen<br/>- Event/Offer listings screen<br/>- Overview of Event/Offer screen<br/>- Chat/Stream for Event/Offer<br/>- Directions for Event/Offer<br/>- Create Event/Offer screen(s)<br/><br/>Will require the design to have a google material feel. <br/><br/>See Attached files for further details

Requirements
Must have
• See Doc
Nice to have
• See Doc
Should not have
• See Doc

```html
<!DOCTYPE html>
<html lang="en">
<head>
<meta charset="utf-8">
<title>Quillo App – Screens</title>
<link rel="stylesheet" href="https://fonts.googleapis.com/css2?family=Roboto:wght@400;500;700;900&family=Roboto+Condensed:wght@700&display=swap">
<style>
:root{
  --page:#f1f5f9;
  --teal:#7dd5dd;
  --teal-title:#6fd3da;
  --yellow:#efdb62;
  --pink:#e8b2e6;
  --pink-soft:#f2c7f2;
  --pink-accent:#e79fe6;
  --ink:#222;
  --grey:#777;
  --white:#fff;
}
*{box-sizing:border-box;margin:0;padding:0}
html,body{width:1200px;height:2433px;overflow:hidden;background:var(--page);font-family:'Roboto',sans-serif;color:var(--ink)}
.board{position:relative;width:1200px;height:2433px}
.screen{position:absolute;overflow:hidden;box-shadow:0 6px 24px rgba(40,60,90,.08)}
.landing{width:441px;height:1053px;background:var(--white)}
.landing.right{left:639px;top:155px}
.device-flat{position:absolute;left:138px;top:118px;width:416px;height:894px;border-radius:44px;overflow:hidden;background:var(--white);box-shadow:0 6px 24px rgba(40,60,90,.1)}
.device-flat .landing{position:absolute;left:0;top:0;transform:scale(.943);transform-origin:0 0;box-shadow:none}

.hero{position:absolute;left:0;top:0;width:441px;height:353px;background:linear-gradient(160deg,#5b6470 0%,#3b3a40 45%,#2a2628 100%)}
.brand{position:absolute;left:0;width:100%;text-align:center;font-family:'Roboto',sans-serif;font-weight:900;letter-spacing:1px}
.hero .brand{top:72px;font-size:66px;color:var(--teal-title)}
.count{position:absolute;top:220px;width:120px;text-align:center;color:var(--white)}
.count b{display:block;font-family:'Roboto Condensed',sans-serif;font-size:47px;color:var(--pink-accent);line-height:1}
.count span{display:block;font-size:18px;margin-top:8px}
.section-title{position:absolute;left:14px;top:394px;font-family:'Roboto Condensed',sans-serif;font-size:35px;color:var(--ink)}
.pager{position:absolute;left:370px;top:400px}
.event-photo{position:absolute;left:15px;top:474px;width:412px;height:169px;background:linear-gradient(120deg,#3a2a1e,#8a6238 50%,#2c2118)}
.date{position:absolute;left:367px;top:474px;width:60px;height:55px;background:var(--pink-accent);color:var(--white);text-align:center;font-family:'Roboto Condensed',sans-serif;line-height:1}
.date small{display:block;font-size:16px;margin-top:6px}
.date b{display:block;font-size:24px}
.avatar{position:absolute;border-radius:50%;background:linear-gradient(150deg,#c9d3dc,#6d7784)}
.organizer{position:absolute;left:90px;top:683px;font-size:17px;color:var(--grey)}
.organizer em{font-style:normal;color:var(--pink-accent)}
.comments{position:absolute;left:360px;top:683px;font-size:17px;color:var(--grey);display:flex;align-items:center;gap:8px}
.btn{position:absolute;left:26px;width:391px;height:62px;display:flex;align-items:center;justify-content:center;gap:10px;color:var(--white);font-family:'Roboto Condensed',sans-serif;font-size:23px;letter-spacing:.3px}
.btn.teal{background:var(--teal)}
.btn.yellow{background:var(--yellow)}
.btn.pink{background:var(--pink)}

.panel{width:441px;background:var(--pink)}
.panel .brand{top:24px;font-size:62px;color:var(--white)}
.panel-bar{position:absolute;left:0;top:109px;width:100%;height:77px;background:var(--teal);display:flex;align-items:center;padding-left:62px;gap:30px;color:var(--white);font-family:'Roboto Condensed',sans-serif;font-size:36px}
.search{left:121px;top:1098px;height:946px}
.field{position:absolute;left:26px;width:391px;height:62px;background:var(--white);display:flex;align-items:center;justify-content:space-between;padding:0 30px;font-size:20px;color:#333}
.chat{left:639px;top:1258px;height:1068px}
.bubble{position:absolute;width:282px;height:88px;background:var(--pink-soft);padding:16px 32px;font-size:20px;line-height:30px;color:#333}
.bubble::before{content:"";position:absolute;top:18px;border:12px solid transparent}
.bubble.in::before{left:-24px;border-right-color:var(--pink-soft);border-top-width:30px;border-bottom-width:0}
.bubble.out::before{right:-24px;border-left-color:var(--pink-soft);border-top-width:30px;border-bottom-width:0}
.time{position:absolute;font-size:16px;color:#333}
.composer{position:absolute;left:16px;top:949px;width:409px;height:66px;border-radius:33px;background:#dea2dc;display:flex;align-items:center;padding:0 22px;gap:16px;color:var(--white);font-size:18px}
.composer .grow{flex:1}
</style>
</head>
<body>
<div class="board">

  <div class="device-flat">
    <section class="landing">
      <div class="hero" role="img" aria-label="Photo of a crowd of guests at a party"></div>
      <div class="brand">Quillo</div>
      <div class="count" style="left:26px"><b>48</b><span>HOURS</span></div>
      <div class="count" style="left:160px"><b>24</b><span>MINUTES</span></div>
      <div class="count" style="left:296px"><b>50</b><span>SECS</span></div>
      <h2 class="section-title">NEAREST EVENTS</h2>
      <svg class="pager" width="44" height="24" viewBox="0 0 44 24" fill="none" stroke="#222" stroke-width="2.5"><path d="M12 3 3 12l9 9M32 3l9 9-9 9"/></svg>
      <div class="event-photo" role="img" aria-label="Photo of friends toasting at an evening event"></div>
      <div class="date"><small>MAR</small><b>09</b></div>
      <div class="avatar" role="img" aria-label="Organizer portrait" style="left:16px;top:659px;width:60px;height:60px"></div>
      <div class="organizer">Organized by <em>Mara Lind</em></div>
      <div class="comments"><svg width="20" height="16" viewBox="0 0 20 16"><ellipse cx="10" cy="7" rx="10" ry="7" fill="#7dd5dd"/><path d="M3 11 1 16l7-3z" fill="#7dd5dd"/></svg>13</div>
      <div class="btn teal" style="top:771px"><svg width="22" height="22" viewBox="0 0 22 22" fill="none" stroke="#fff" stroke-width="2"><rect x="2" y="4" width="18" height="16" rx="2"/><path d="M2 9h18M7 1v5M15 1v5"/></svg>START AN EVENT</div>
      <div class="btn yellow" style="top:853px"><svg width="22" height="22" viewBox="0 0 22 22" fill="none" stroke="#fff" stroke-width="3"><circle cx="9" cy="9" r="7"/><path d="m14 14 6 6"/></svg>SEARCH FOR EVENTS</div>
    </section>
  </div>

  <section class="screen landing right">
    <div class="hero" role="img" aria-label="Photo of a crowd of guests at a party"></div>
    <div class="brand">Quillo</div>
    <div class="count" style="left:26px"><b>48</b><span>HOURS</span></div>
    <div class="count" style="left:160px"><b>24</b><span>MINUTES</span></div>
    <div class="count" style="left:296px"><b>50</b><span>SECS</span></div>
    <h2 class="section-title">NEAREST EVENTS</h2>
    <svg class="pager" width="44" height="24" viewBox="0 0 44 24" fill="none" stroke="#222" stroke-width="2.5"><path d="M12 3 3 12l9 9M32 3l9 9-9 9"/></svg>
    <div class="event-photo" role="img" aria-label="Photo of friends toasting at an evening event"></div>
    <div class="date"><small>MAR</small><b>09</b></div>
    <div class="avatar" role="img" aria-label="Organizer portrait" style="left:16px;top:659px;width:60px;height:60px"></div>
    <div class="organizer">Organized by <em>Mara Lind</em></div>
    <div class="comments"><svg width="20" height="16" viewBox="0 0 20 16"><ellipse cx="10" cy="7" rx="10" ry="7" fill="#7dd5dd"/><path d="M3 11 1 16l7-3z" fill="#7dd5dd"/></svg>13</div>
    <div class="btn teal" style="top:771px"><svg width="22" height="22" viewBox="0 0 22 22" fill="none" stroke="#fff" stroke-width="2"><rect x="2" y="4" width="18" height="16" rx="2"/><path d="M2 9h18M7 1v5M15 1v5"/></svg>START AN EVENT</div>
    <div class="btn yellow" style="top:853px"><svg width="22" height="22" viewBox="0 0 22 22" fill="none" stroke="#fff" stroke-width="3"><circle cx="9" cy="9" r="7"/><path d="m14 14 6 6"/></svg>SEARCH FOR EVENTS</div>
    <div class="btn pink" style="top:936px"><svg width="20" height="22" viewBox="0 0 20 22" fill="#fff"><circle cx="10" cy="6" r="5"/><path d="M0 22c0-7 4-10 10-10s10 3 10 10z"/></svg>LOGIN</div>
  </section>

  <section class="screen panel search">
    <div class="brand">Quillo</div>
    <div class="panel-bar"><svg width="20" height="36" viewBox="0 0 20 36" fill="none" stroke="#fff" stroke-width="4"><path d="M17 2 3 18l14 16"/></svg>EVENT SEARCH</div>
    <div class="field" style="top:226px">Location search</div>
    <div class="field" style="top:308px">Distance</div>
    <div class="field" style="top:390px">Friends</div>
    <div class="field" style="top:473px">Category</div>
    <div class="field" style="top:555px">Start time<svg width="20" height="12" viewBox="0 0 20 12" fill="none" stroke="#333" stroke-width="2.5"><path d="m2 2 8 8 8-8"/></svg></div>
    <div class="field" style="top:638px">No of attendees</div>
    <div class="field" style="top:720px">No of offers</div>
    <div class="btn yellow" style="top:804px"><svg width="22" height="22" viewBox="0 0 22 22" fill="none" stroke="#fff" stroke-width="3"><circle cx="9" cy="9" r="7"/><path d="m14 14 6 6"/></svg>SEARCH</div>
  </section>

  <section class="screen panel chat">
    <div class="brand">Quillo</div>
    <div class="panel-bar"><svg width="20" height="36" viewBox="0 0 20 36" fill="none" stroke="#fff" stroke-width="4"><path d="M17 2 3 18l14 16"/></svg>EVENT CHAT</div>

    <div class="avatar" role="img" aria-label="Guest portrait" style="left:38px;top:239px;width:60px;height:60px"></div>
    <div class="bubble in" style="left:122px;top:239px">Lorem ipsum dolor sit amonseet</div>
    <div class="time" style="right:36px;top:343px">4:30 PM</div>

    <div class="bubble out" style="left:36px;top:414px">Lorem ipsum dolor sit amonseet</div>
    <div class="avatar" role="img" aria-label="Guest portrait" style="left:344px;top:414px;width:60px;height:60px"></div>
    <div class="time" style="left:36px;top:518px">4:30 PM</div>

    <div class="avatar" role="img" aria-label="Guest portrait" style="left:38px;top:590px;width:60px;height:60px"></div>
    <div class="bubble in" style="left:122px;top:590px">Lorem ipsum dolor sit amonseet</div>
    <div class="time" style="right:36px;top:694px">4:30 PM</div>

    <div class="bubble out" style="left:36px;top:765px">Lorem ipsum dolor sit amonseet</div>
    <div class="avatar" role="img" aria-label="Guest portrait" style="left:344px;top:765px;width:60px;height:60px"></div>
    <div class="time" style="left:36px;top:869px">4:30 PM</div>

    <div class="composer">
      <svg width="32" height="32" viewBox="0 0 32 32" fill="none" stroke="#fff" stroke-width="2"><circle cx="16" cy="16" r="14"/><circle cx="11" cy="13" r="1.5" fill="#fff"/><circle cx="21" cy="13" r="1.5" fill="#fff"/><path d="M9 19c4 5 10 5 14 0"/></svg>
      <span class="grow">Send Message</span>
      <svg width="26" height="26" viewBox="0 0 26 26" fill="none" stroke="#fff" stroke-width="2"><path d="M20 12 11 21a5 5 0 0 1-7-7L14 4a3.5 3.5 0 0 1 5 5L9 19a2 2 0 0 1-3-3l9-9"/></svg>
      <svg width="30" height="26" viewBox="0 0 30 26" fill="#fff"><path d="M3 6h6l3-4h6l3 4h6v18H3z"/><circle cx="15" cy="15" r="5" fill="#dea2dc"/></svg>
    </div>
  </section>

</div>
</body>
</html>
```